I am a general contractor in Portland, Or. I would like a clean and simple design layout, maybe using the "didot" font, blue and dark bronze in colors are preferred. On one side of the card, it would be nice to have a logo(attached photo) and business name(KLM Construction). I don't need my job title on the card, just some thing along the lines of "oliver kemp, general contractor". Thanks much.

Target Market(s)

Adults from 30-55 years old. Middle to upper class.

Industry/Entity Type

Contractor

Contact Information for Business Card

KLM Construction
Oliver T. Kemp
2843 NE 71st Ave.
Portland, Or. 97348
503.962.7084

Font styles to use
Other font styles liked:
• didot

Colors
3277b5
7f7f7f

Requirements
Should not have
• Too much going on.

```html
<!DOCTYPE html>
<html lang="en">
<head>
<meta charset="utf-8">
<title>Brevik Construction – Business Card</title>
<link rel="stylesheet" href="https://fonts.googleapis.com/css2?family=Bodoni+Moda:wght@400&display=swap">
<style>
  :root {
    --brand-blue: #2f76b6;
    --text-grey: #7f7f7f;
    --card-white: #ffffff;
  }
  html, body {
    margin: 0;
    padding: 0;
    width: 1200px;
    height: 703px;
    overflow: hidden;
    background: var(--card-white);
  }
  .card {
    position: relative;
    width: 1200px;
    height: 703px;
    background: var(--card-white);
    font-family: "Bodoni Moda", "Didot", "Times New Roman", serif;
    font-weight: 400;
  }
  .brand-mark {
    position: absolute;
    left: 52px;
    top: 204px;
    width: 400px;
    height: 90px;
    display: flex;
    align-items: center;
    justify-content: center;
    font-size: 68px;
    line-height: 1;
    color: var(--brand-blue);
    white-space: nowrap;
  }
  .company-name {
    position: absolute;
    right: 52px;
    top: 76px;
    margin: 0;
    font-size: 70px;
    font-weight: 400;
    line-height: 1;
    color: var(--brand-blue);
    white-space: nowrap;
  }
  .contact {
    position: absolute;
    right: 52px;
    top: 414px;
    text-align: right;
    color: var(--text-grey);
  }
  .contact-name {
    margin: 0 0 24px;
    font-size: 54px;
    line-height: 1;
    white-space: nowrap;
  }
  .contact-line {
    margin: 0;
    font-size: 33px;
    line-height: 46px;
    white-space: nowrap;
  }
  .footer-band {
    position: absolute;
    left: 0;
    bottom: 0;
    width: 1200px;
    height: 72px;
    background: var(--brand-blue);
  }
</style>
</head>
<body>
  <div class="card">
    <div class="brand-mark">Brevik</div>
    <h1 class="company-name">Brevik Construction</h1>
    <div class="contact">
      <p class="contact-name">Oliver T. Kemp</p>
      <p class="contact-line">2843 NE 71st Ave. Portland, Or. 97348</p>
      <p class="contact-line">503.962.7084</p>
    </div>
    <div class="footer-band"></div>
  </div>
</body>
</html>
```